real esate business card with company logo and name

we need a business card design for a real esate company

The company name is Walsh & Brody Pty Ltd, and we have our logo designed and will upload. We want classic or moden feel. Black or white background. looks more textured. Should include folowinginformations
Paul Walsh and Lucy Brody
Sales Agents & Onsite Manager
p: 07 5948 2063
F: 07 5948 2174
M:0461 857 239
3/42 Marlin Crescent, ELLEN GROVE QLD 4078

We want this business card looks professonal. Thank you in advance.

Industry/Entity Type

Real Estate Agent

Contact Information for Business Card

Paul Walsh and Lucy Brody
Onsite Manager & Sales Agents
p: 07 5948 2063
M:0461 857 239

Font styles to use
Serif

Colors
000000
fbfbfb
333333
959595

Requirements
Must have
• company logo and name, black or white back ground

```html
<!DOCTYPE html>
<html lang="en">
<head>
<meta charset="utf-8">
<title>Walsh &amp; Brody Pty Ltd — Business Cards</title>
<link rel="stylesheet" href="https://fonts.googleapis.com/css2?family=Tinos:ital,wght@0,400;0,700;1,400&display=swap">
<style>
  :root {
    --black: #000000;
    --paper: #fbfbfb;
    --charcoal: #333333;
    --grey: #959595;
    --white: #ffffff;
    --edge: #b5b5b5;
  }
  * { margin: 0; padding: 0; box-sizing: border-box; }
  html, body {
    width: 1200px;
    height: 1200px;
    overflow: hidden;
    background: var(--white);
    font-family: "Tinos", "Times New Roman", serif;
  }
  .canvas { position: relative; width: 1200px; height: 1200px; }

  .card {
    position: absolute;
    left: 286px;
    width: 618px;
    height: 354px;
    overflow: hidden;
  }
  .card--front { top: 193px; background: var(--black); color: var(--white); }
  .card--back  { top: 658px; background: var(--paper); color: var(--charcoal); border: 1px solid var(--edge); }

  .card__band-dark  { position: absolute; left: 0; top: 0; width: 100%; height: 10px; background: var(--charcoal); }
  .card__band-light { position: absolute; left: 0; top: 10px; width: 100%; height: 11px; background: var(--grey); }

  .brand {
    position: absolute;
    left: 52px;
    top: 125px;
    width: 200px;
    text-align: center;
  }
  .brand__square {
    display: block;
    width: 80px;
    height: 80px;
    margin: 0 auto 30px;
    background: var(--grey);
  }
  .brand__name {
    font-size: 14px;
    line-height: 16px;
    letter-spacing: 0.5px;
    color: var(--grey);
    white-space: nowrap;
  }

  .details {
    position: absolute;
    left: 298px;
    top: 87px;
    line-height: 34.4px;
    font-size: 16px;
    white-space: nowrap;
  }
  .details__names { font-size: 21px; font-weight: 700; line-height: 28px; margin-bottom: 4px; }
  .details__role  { font-size: 17.5px; font-style: italic; }
</style>
</head>
<body>
<main class="canvas">

  <section class="card card--front">
    <div class="card__band-dark"></div>
    <div class="card__band-light"></div>
    <div class="brand">
      <span class="brand__square"></span>
      <p class="brand__name">WALSH &amp; BRODY PTY LTD.</p>
    </div>
    <div class="details">
      <p class="details__names">Paul Walsh and Lucy Brody</p>
      <p class="details__role">Onsite Manager &amp; Sales Agents</p>
      <p>p: 07 5948 2063</p>
      <p>M:0461 857 239</p>
      <p>3/42 Marlin Crescent,</p>
      <p>CORAL DOWNS QLD 4215</p>
    </div>
  </section>

  <section class="card card--back">
    <div class="card__band-dark"></div>
    <div class="card__band-light"></div>
    <div class="brand">
      <span class="brand__square"></span>
      <p class="brand__name">WALSH &amp; BRODY PTY LTD.</p>
    </div>
    <div class="details">
      <p class="details__names">Paul Walsh and Lucy Brody</p>
      <p class="details__role">Onsite Manager &amp; Sales Agents</p>
      <p>p: 07 5948 2063</p>
      <p>M:0461 857 239</p>
      <p>3/42 Marlin Crescent,</p>
      <p>CORAL DOWNS QLD 4215</p>
    </div>
  </section>

</main>
</body>
</html>
```